KelvrasMassage website required

We need a website for a mobile sports massage therapist in the United Kingdom. Specialising in pregnancy and postnatal massage, sports and remedial, deep tissue massage & Corprate Massage. Attached are some logos that we already have in various colours. The file named logo_white_background is what we normally use. Feel free to use the others at your discretion.

Requirements
Must have
• Service areas, Booking system.

```html
<!DOCTYPE html>
<html lang="en">
<head>
<meta charset="utf-8">
<title>Kelvra's Massage</title>
<link href="https://fonts.googleapis.com/css2?family=Raleway:ital,wght@0,300;0,400;0,500;0,600;0,700;0,800;1,300;1,400&family=Great+Vibes&display=swap" rel="stylesheet">
<style>
:root{
  --blue:#00a9ec;
  --sky:#6ccbf7;
  --sky-soft:#8fd7fa;
  --mint:#00f282;
  --grey:#7b7b7b;
  --grey-light:#c4c4c4;
  --ink:#4a4a4a;
  --white:#ffffff;
}
*{box-sizing:border-box;margin:0;padding:0}
html,body{width:1200px;height:3315px;overflow:hidden}
body{font-family:'Raleway',sans-serif;color:var(--ink);background:var(--white);position:relative}
.script{font-family:'Great Vibes',cursive;font-weight:400}

/* Header */
.site-header{position:absolute;left:0;top:0;width:1200px;height:172px;background:var(--white)}
.main-nav{position:absolute;left:51px;top:124px;display:flex;gap:18px;font-size:22px;color:#555;white-space:nowrap}
.brand-badge{position:absolute;left:491px;top:0;width:212px;height:212px;border-radius:50%;background:var(--white);border:5px solid var(--sky);display:flex;align-items:center;justify-content:center;z-index:3;text-align:center}
.brand-badge span{font-size:27px;font-weight:600;color:var(--sky);line-height:1.2}
.header-social{position:absolute;right:50px;top:27px;display:flex;gap:11px}
.header-social i{width:26px;height:26px;background:var(--blue);border-radius:3px;display:block}
.header-contact{position:absolute;right:50px;top:92px;text-align:right;font-size:22px;font-weight:600;color:#555;line-height:34px}
.header-contact div{display:flex;justify-content:flex-end;align-items:center;gap:10px}

/* Hero */
.hero{position:absolute;left:0;top:172px;width:1200px;height:741px}
.hero-photo{position:absolute;inset:0;background:linear-gradient(115deg,#9fbf93 0%,#c9d3b1 28%,#e5d9c6 52%,#bfae97 75%,#8c7c68 100%)}
.hero-copy{position:absolute;left:300px;top:165px;width:640px;text-align:center;color:var(--white)}
.hero-copy .lead{font-size:33px;font-weight:600;line-height:40px}
.hero-copy .accent{font-size:54px;font-weight:800;color:var(--blue);line-height:56px;letter-spacing:1px}
.hero-copy p{font-size:21px;line-height:28px;margin-top:38px;padding:0 18px}
.btn{display:inline-flex;align-items:center;justify-content:center;border-radius:36px;font-size:21px;font-weight:600;color:var(--white);letter-spacing:.5px;white-space:nowrap}
.hero-actions{position:absolute;left:398px;top:482px;display:flex;gap:28px}
.btn-solid{width:188px;height:70px;background:var(--blue)}
.btn-ghost{width:188px;height:70px;border:3px solid var(--white)}

/* Services */
.services-band{position:absolute;left:0;top:913px;width:1200px;height:99px;background:var(--blue);color:var(--white);text-align:center;font-size:60px;line-height:99px}
.service-grid{position:absolute;left:0;top:1012px;width:1200px;height:354px;display:flex;gap:4px}
.service-tile{flex:1;position:relative}
.service-tile .photo{position:absolute;inset:0}
.service-tile .label{position:absolute;left:0;right:0;bottom:0;height:88px;background:rgba(80,190,240,.72);color:var(--white);font-size:22px;font-weight:700;display:flex;align-items:center;justify-content:center}

/* Testimonials */
.testimonials{position:absolute;left:0;top:1366px;width:1200px;height:442px;text-align:center}
.testimonials h2{font-size:56px;color:var(--sky);position:absolute;top:40px;width:100%}
.quote-mark{position:absolute;font-size:190px;color:var(--grey-light);font-family:Georgia,serif;line-height:1}
.quote-text{position:absolute;left:310px;top:118px;width:580px;font-size:32px;font-style:italic;font-weight:300;color:var(--grey);line-height:41px;white-space:nowrap}
.quote-author{position:absolute;top:334px;width:100%;font-size:33px;font-weight:600;color:var(--grey);line-height:42px}
.dots{position:absolute;top:397px;left:0;width:100%;display:flex;justify-content:center;gap:22px}
.dots i{width:18px;height:18px;border-radius:50%;background:var(--grey-light);display:block}
.dots i.on{background:var(--grey)}

/* Booking */
.booking{position:absolute;left:0;top:1808px;width:1200px;height:398px;background:linear-gradient(100deg,var(--mint) 0%,#40dfb6 40%,#5bd6e6 65%,var(--sky) 100%);color:var(--white);text-align:center}
.booking h2{font-size:58px;position:absolute;top:22px;width:100%}
.booking p{position:absolute;left:320px;top:98px;width:560px;font-size:21px;line-height:27px}
.field{position:absolute;background:var(--white);border-radius:30px;font-size:14px;font-style:italic;color:#999;padding-left:28px;display:flex;align-items:center;text-align:left}
.booking .btn{position:absolute;left:491px;top:316px;width:188px;height:57px;border:3px solid var(--white);font-size:21px}

/* Blog */
.blog{position:absolute;left:0;top:2206px;width:1200px;height:570px}
.blog h2{position:absolute;left:53px;top:28px;font-size:58px;color:var(--sky)}
.post{position:absolute;top:121px;width:346px}
.post .photo{height:254px}
.post h3{font-size:28px;font-weight:600;color:#666;margin-top:28px}
.post .meta{display:flex;justify-content:space-between;font-size:13px;font-style:italic;color:#777;margin-top:6px}
.post p{font-size:20px;color:#777;line-height:29px;margin-top:6px;white-space:nowrap}

/* Footer */
.site-footer{position:absolute;left:0;top:2776px;width:1200px;height:539px;background:var(--sky);color:var(--white)}
.footer-social{position:absolute;left:53px;top:44px;display:flex;gap:20px}
.footer-social i{width:60px;height:60px;border:5px solid var(--white);border-radius:8px;display:block}
.footer-line{position:absolute;left:53px;display:flex;gap:30px;font-size:21px;line-height:27px;font-weight:500}
.footer-brand{position:absolute;left:53px;top:360px;width:280px;text-align:center;font-size:36px;font-weight:700;line-height:44px}
.copyright{position:absolute;left:57px;top:472px;font-size:21px;line-height:27px}
.site-footer h2{position:absolute;left:616px;top:50px;font-size:56px}
.site-footer .field{color:var(--sky)}
.submit{position:absolute;left:990px;top:468px;width:160px;height:47px;border:3px solid var(--white);font-size:21px}
</style>
</head>
<body>

<header class="site-header">
  <nav class="main-nav"><span>HOME</span><span>ABOUT</span><span>SERVICES</span><span>CONTACT</span></nav>
  <div class="brand-badge"><span>Kelvra's<br>Massage</span></div>
  <div class="header-social"><i></i><i></i><i></i><i></i><i></i></div>
  <div class="header-contact">
    <div><svg width="22" height="22" viewBox="0 0 24 24"><path fill="#555" d="M6.6 10.8a15 15 0 0 0 6.6 6.6l2.2-2.2c.3-.3.7-.4 1-.2 1.1.4 2.3.6 3.6.6.6 0 1 .4 1 1V20c0 .6-.4 1-1 1A17 17 0 0 1 3 4c0-.6.4-1 1-1h3.5c.6 0 1 .4 1 1 0 1.3.2 2.5.6 3.6.1.3 0 .7-.2 1z"/></svg>(1800) 4270 552 19</div>
    <div><svg width="24" height="18" viewBox="0 0 24 18"><rect width="24" height="18" rx="2" fill="#555"/><path d="M1 2l11 8 11-8" stroke="#fff" stroke-width="2" fill="none"/></svg>support@kelvrasmassage.com</div>
  </div>
</header>

<section class="hero">
  <div class="hero-photo" role="img" aria-label="Photo of a woman relaxing while receiving a back massage, with orchids on the table"></div>
  <div class="hero-copy">
    <div class="lead">Soothing with</div>
    <div class="accent">WARMTH</div>
    <div class="lead">of hands</div>
    <p>Lorem ipsum dolor sit amet, consectetur adipisicing elit, sed do eiusmod tempor incididunt ut labore et dolore magna aliqua. Ut enim ad minim veniam, quis nostrud</p>
  </div>
  <div class="hero-actions"><span class="btn btn-solid">BOOK NOW</span><span class="btn btn-ghost">LEARN MORE</span></div>
</section>

<h2 class="services-band script">Services</h2>
<section class="service-grid">
  <article class="service-tile">
    <div class="photo" role="img" aria-label="Photo of hands massaging a pregnant belly" style="background:linear-gradient(135deg,#f3ded0,#d9a98d 60%,#f1ece6)"></div>
    <div class="label">Pregnancy &amp; Postnatal Massage</div>
  </article>
  <article class="service-tile">
    <div class="photo" role="img" aria-label="Photo of a therapist stretching a client's leg" style="background:linear-gradient(135deg,#e8e4e0,#9d9a97 55%,#3b3f46)"></div>
    <div class="label">Sports &amp; Remedial Massage</div>
  </article>
  <article class="service-tile">
    <div class="photo" role="img" aria-label="Photo of a deep tissue massage with bamboo sticks" style="background:linear-gradient(135deg,#1e6f83,#8a5a3c 55%,#c98c67)"></div>
    <div class="label">Deep Tissue Massage</div>
  </article>
</section>

<section class="testimonials">
  <h2 class="script">Testimonials</h2>
  <span class="quote-mark" style="left:262px;top:100px">&ldquo;</span>
  <blockquote class="quote-text">Lorem ipsum dolor sit amet, con-<br>sectetur adipisicing elit, sed do ei-<br>usmod tempor incididunt ut labore<br>et dolore magna aliqua. Ut enim<br>ad minim veniam, quis nostrud ex-</blockquote>
  <span class="quote-mark" style="left:868px;top:222px">&rdquo;</span>
  <div class="quote-author">-John Doe</div>
  <div class="dots"><i></i><i class="on"></i><i></i></div>
</section>

<section class="booking">
  <h2 class="script">Book your session!</h2>
  <p>Fill in the form below to book your session. It only takes minutes!</p>
  <div class="field" style="left:398px;top:170px;width:376px;height:58px">Full Name*</div>
  <div class="field" style="left:398px;top:243px;width:376px;height:60px">Email Address*</div>
  <span class="btn">BOOK NOW!</span>
</section>

<section class="blog">
  <h2 class="script">From the blog</h2>
  <article class="post" style="left:53px">
    <div class="photo" role="img" aria-label="Photo of a foot massage" style="background:linear-gradient(135deg,#b7a79a,#e2b79b 50%,#c8845f)"></div>
    <h3>Blog Post Title</h3>
    <div class="meta"><span>by admin</span><span>7/16/2018</span></div>
    <p>Lorem ipsum dolor sit amet, con-<br>sectetur adipisicing elit, sed do</p>
  </article>
  <article class="post" style="left:429px">
    <div class="photo" role="img" aria-label="Photo of a woman receiving a face and neck massage" style="background:linear-gradient(135deg,#d3a57f,#f0dccb 55%,#e9e3dc)"></div>
    <h3>Blog Post Title</h3>
    <div class="meta"><span>by admin</span><span>7/16/2018</span></div>
    <p>Lorem ipsum dolor sit amet, con-<br>sectetur adipisicing elit, sed do</p>
  </article>
  <article class="post" style="left:804px">
    <div class="photo" role="img" aria-label="Photo of a hot stone massage on a back" style="background:linear-gradient(135deg,#d9d2c6,#c7a487 55%,#9c7a5f)"></div>
    <h3>Blog Post Title</h3>
    <div class="meta"><span>by admin</span><span>7/16/2018</span></div>
    <p>Lorem ipsum dolor sit amet, con-<br>sectetur adipisicing elit, sed do</p>
  </article>
</section>

<footer class="site-footer">
  <div class="footer-social"><i></i><i></i><i></i><i></i><i></i></div>
  <div class="footer-line" style="top:148px">
    <svg width="36" height="50" viewBox="0 0 24 34"><path fill="#fff" d="M12 0A12 12 0 0 0 0 12c0 9 12 22 12 22s12-13 12-22A12 12 0 0 0 12 0zm0 17a5 5 0 1 1 0-10 5 5 0 0 1 0 10z"/></svg>
    <span>218 Harrow Lane, Westbrook,<br>Ashford</span>
  </div>
  <div class="footer-line" style="top:226px">
    <svg width="40" height="44" viewBox="0 0 24 24"><path fill="#fff" d="M6.6 10.8a15 15 0 0 0 6.6 6.6l2.2-2.2c.3-.3.7-.4 1-.2 1.1.4 2.3.6 3.6.6.6 0 1 .4 1 1V20c0 .6-.4 1-1 1A17 17 0 0 1 3 4c0-.6.4-1 1-1h3.5c.6 0 1 .4 1 1 0 1.3.2 2.5.6 3.6.1.3 0 .7-.2 1z"/></svg>
    <span>(100) 240 3386 57190<br>(977) 61 820 437</span>
  </div>
  <div class="footer-brand">Kelvra's<br>Massage</div>
  <div class="copyright">Copyright &copy; 2018, Kelvra's Massage</div>

  <h2 class="script">Contact Form</h2>
  <div class="field" style="left:614px;top:141px;width:252px;height:49px">Full Name*</div>
  <div class="field" style="left:895px;top:141px;width:255px;height:49px">Email Address*</div>
  <div class="field" style="left:614px;top:210px;width:536px;height:236px;align-items:flex-start;padding-top:16px;border-radius:22px">Message*</div>
  <span class="btn submit">SUBMIT</span>
</footer>

</body>
</html>
```